High-end construction company needs a business card design

We need a modern looking business card that draws people in, is memorable and looks so good people will want to sick it on their fridges.
On the first side what is needed are:
Logo
My name - Tomas Verbelk
Title - Managing Director
Website - www.kravel.co.uk
Email - tomas@kravel.co.uk
Telephone - 020 5194 6381
Mobile - 07845319027
On the back side was is needed is a list of all the services we provide:
-Kitchen Renovations
-Bathroom Renovations
-House Renovations
-Garage Conversions
-Extensions
-Loft Conversions
-Conservatories
-Carpentry
-Tiling
-Electrical
-Plumbing & Heating
-Bricklaying
-Landscaping
-Decorating
-Plastering
We would like the colours to be the same shades as on the logo with grey or black for the words.
Target Market(s)
Anyone who needs building work done
Contact Information for Business Card
This business card is for a construction company which strives to deliver excellent service and quality.
The look and feel of the card should represent this.
Requirements
Must have
- On the first side what is needed are:
Logo
My name - Tomas Verbelk
Title - Managing Director
Website - www.kravel.co.uk
Email - tomas@kravel.co.uk
Telephone - 020 5194 6381
Mobile - 07845319027
Nice to have
- Cool looking features

```html
<!DOCTYPE html>
<html lang="en">
<head>
<meta charset="utf-8">
<title>Kravel Construction Ltd – Business Card</title>
<link href="https://fonts.googleapis.com/css2?family=Open+Sans:wght@400;700&display=swap" rel="stylesheet">
<style>
  :root {
    --bg: #ebebeb;
    --green-light: #72bf44;
    --green-dark: #4a8c3f;
    --band-light: #dfe9d9;
    --ink: #1f1f1f;
  }
  * { margin: 0; padding: 0; box-sizing: border-box; }
  html, body { width: 1000px; height: 1200px; overflow: hidden; background: var(--bg); }
  body { position: relative; font-family: "Open Sans", Arial, sans-serif; color: var(--ink); }

  .card {
    position: absolute; left: 104px; width: 810px; height: 462px;
    background: var(--green-light);
    border: 10px solid var(--green-dark);
    overflow: hidden;
  }
  .card--front { top: 118px; }
  .card--back { top: 623px; }

  .front-arc {
    position: absolute; left: -264px; top: -20px;
    width: 638px; height: 482px; border-radius: 50%;
    background: var(--green-dark);
  }
  .front-band {
    position: absolute; left: 300px; right: 0; top: 90px; height: 80px;
    background: linear-gradient(90deg, var(--green-dark) 0%, var(--band-light) 45%, var(--band-light) 55%, var(--green-dark) 100%);
  }
  .wordmark {
    position: absolute; left: 68px; top: 232px; width: 260px;
    font-weight: 700; color: var(--ink); text-align: center; line-height: 1;
  }
  .wordmark__name { display: block; font-size: 56px; letter-spacing: 1px; }
  .wordmark__sub { display: block; font-size: 14px; letter-spacing: 2.4px; margin-top: 6px; }

  .person { position: absolute; left: 426px; top: 102px; }
  .person__name { font-size: 28px; font-weight: 700; letter-spacing: 1px; line-height: 1.1; }
  .person__title { font-size: 18px; letter-spacing: 1.6px; margin-top: 2px; }

  .contacts { position: absolute; left: 424px; top: 222px; list-style: none; }
  .contacts li { display: flex; align-items: center; height: 35.5px; font-size: 23px; letter-spacing: 1px; }
  .contacts svg { width: 20px; height: 20px; margin-right: 18px; fill: var(--ink); }

  .back-band {
    position: absolute; left: 0; right: 0; top: 54px; height: 40px;
    background: linear-gradient(90deg, var(--green-dark) 0%, var(--band-light) 50%, var(--green-dark) 100%);
    display: flex; align-items: center; justify-content: center;
  }
  .back-band h2 { font-size: 28px; font-weight: 700; color: #111; }

  .services { position: absolute; top: 136px; list-style: none; }
  .services--left { left: 92px; }
  .services--right { left: 445px; }
  .services li { font-size: 23px; height: 30.8px; line-height: 30.8px; display: flex; align-items: center; letter-spacing: 0.4px; }
  .services li::before {
    content: ""; width: 13px; height: 13px; border-radius: 50%;
    background: #111; margin-right: 10px; flex: none;
  }
</style>
</head>
<body>
  <section class="card card--front">
    <div class="front-arc"></div>
    <div class="front-band"></div>
    <div class="wordmark">
      <span class="wordmark__name">KRAVEL</span>
      <span class="wordmark__sub">CONSTRUCTION LTD</span>
    </div>
    <div class="person">
      <h1 class="person__name">TOMAS VERBELK</h1>
      <p class="person__title">MANAGING DIRECTOR</p>
    </div>
    <ul class="contacts">
      <li><svg viewBox="0 0 20 20"><path d="M6 2h8v16H6z M8 4v10h4V4z"/></svg>07845319027</li>
      <li><svg viewBox="0 0 20 20"><path d="M5 2l3 4-2 2c1 3 3 5 6 6l2-2 4 3-2 3C8 18 2 12 2 5z"/><path d="M12 3a6 6 0 0 1 5 5h-1.6A4.4 4.4 0 0 0 12 4.6z"/></svg>020 5194 6381</li>
      <li><svg viewBox="0 0 20 20"><path d="M1 4h18v12H1z M3 6v.5l7 5 7-5V6zm0 3v5h14V9l-7 5z"/></svg>TOMAS@KRAVEL.CO.UK</li>
      <li><svg viewBox="0 0 20 20"><circle cx="10" cy="10" r="9"/><path d="M1 10h18M10 1v18M3 5.5h14M3 14.5h14" stroke="#72bf44" stroke-width="1.2" fill="none"/><ellipse cx="10" cy="10" rx="4" ry="9" stroke="#72bf44" stroke-width="1.2" fill="none"/></svg>WWW.KRAVEL.CO.UK</li>
    </ul>
  </section>

  <section class="card card--back">
    <div class="back-band"><h2>SERVICES</h2></div>
    <ul class="services services--left">
      <li>KITCHEN RENOVATIONS</li>
      <li>BATHROOM RENOVATIONS</li>
      <li>HOUSE RENOVATIONS</li>
      <li>GARAGE CONVERSIONS</li>
      <li>EXTENSIONS</li>
      <li>LOFT CONVERSIONS</li>
      <li>CONSERVATORIES</li>
      <li>CARPENTRY</li>
    </ul>
    <ul class="services services--right">
      <li>TILING</li>
      <li>ELECTRICAL</li>
      <li>PLUMBING &amp; HEATING</li>
      <li>BRICKLAYING</li>
      <li>LANDSCAPING</li>
      <li>DECORATING</li>
      <li>PLASTERING</li>
    </ul>
  </section>
</body>
</html>
```